Quenti Peruvian Cuisine needs a take-out menu

We need a new tri-fold 8.5"x11" take out menu for a Peruvian restaurant based in New Rochelle, NY. We have a vast selections of dishes from appetizers, seafood based dishes, desserts, Peruvian ceviches and more. We have attached the following:

Restaurant information
Pictures of our dishes
Quenti Logo in pdf format
Menu in word format
Old take out menu for reference only! (our dishes have changed)
Updates

Industry/Entity Type

Restaurant

```html
<!DOCTYPE html>
<html lang="en">
<head>
<meta charset="utf-8">
<title>Quenti Peruvian Cuisine – Take-Out Menu</title>
<link href="https://fonts.googleapis.com/css2?family=Black+Ops+One&family=Almendra:wght@700&family=Old+Standard+TT:wght@400;700&family=Righteous&display=swap" rel="stylesheet">
<style>
:root{
  --bg:#e9e4dc;
  --green-dark:#3f6d10;
  --green-mid:#5f9a1a;
  --green-bright:#8cc63f;
  --panel-top:#b6df5a;
  --panel-bottom:#e8f05a;
  --yellow:#f2ee24;
  --ink:#1e2a08;
  --title:#f4e53a;
  --red:#e32a1c;
  --white:#ffffff;
}
*{box-sizing:border-box;margin:0;padding:0}
html,body{width:1200px;height:1200px;overflow:hidden;background:var(--bg)}
body{position:relative;font-family:"Old Standard TT",serif;color:var(--ink)}
.sheet{position:absolute;left:210px;width:780px;height:584px;display:grid;grid-template-columns:1fr 1fr 1fr;background:linear-gradient(160deg,var(--green-mid),var(--green-dark));box-shadow:0 4px 14px rgba(0,0,0,.25);overflow:hidden}
.sheet--outside{top:8px}
.sheet--inside{top:604px}
.panel{position:relative;border-right:1px solid rgba(0,0,0,.25);padding:14px 12px;overflow:hidden}
.panel:last-child{border-right:none}
.box{background:linear-gradient(180deg,var(--panel-top),var(--panel-bottom));border-radius:4px;padding:8px 10px 8px;position:relative}
.heading{display:inline-block;font-family:"Black Ops One",sans-serif;font-size:14px;color:var(--ink);background:linear-gradient(180deg,var(--green-bright),var(--green-mid));padding:4px 30px 3px 14px;margin:0 0 6px -18px;box-shadow:2px 2px 3px rgba(0,0,0,.35);letter-spacing:.5px}
.item{margin-bottom:6px}
.row{display:flex;align-items:baseline;font-size:7.4px;font-weight:700;text-transform:uppercase;line-height:1.2}
.row .lead{flex:1;border-bottom:1px dotted var(--ink);margin:0 2px;transform:translateY(-2px)}
.sub{font-weight:400;text-transform:none}
.desc{font-size:6.3px;line-height:1.2}
/* outside */
.outside-1 .box{height:524px}
.photo{position:absolute;border-radius:50%;background:radial-gradient(circle at 40% 40%,#f4efe2,#c98f4b 70%,#7a4a1c);border:5px solid var(--green-bright)}
.photo-1{left:76px;top:8px;width:88px;height:88px}
.photo-2{left:140px;top:110px;width:108px;height:108px}
.photo-strip{position:absolute;left:90px;top:0;width:180px;height:110px;background:linear-gradient(120deg,#f6f2ea,#e9d7bf 50%,#fff);}
.soups{position:absolute;left:12px;right:8px;top:236px;height:306px}
.cover-photo{position:absolute;left:0;right:0;top:0;height:205px;background:linear-gradient(135deg,#fff 20%,#e0a25a 45%,#b9591e 70%,#fff)}
.phone{position:absolute;right:10px;top:14px;display:flex;align-items:center;gap:6px;background:linear-gradient(180deg,var(--green-bright),var(--green-mid));border-radius:20px;padding:4px 6px 4px 14px;border:2px solid var(--green-dark);font-family:"Righteous",sans-serif;font-size:13px;color:var(--ink)}
.phone svg{width:26px;height:26px}
.logo{position:absolute;left:50%;top:176px;transform:translateX(-50%);width:116px;height:116px;border-radius:50%;background:var(--white);border:6px solid var(--green-bright);display:flex;align-items:center;justify-content:center;font-family:"Old Standard TT",serif;font-weight:700;font-size:20px;color:var(--green-dark)}
.cover-title{position:absolute;left:0;right:0;top:302px;text-align:center;font-family:"Almendra",serif;font-size:24px;line-height:1.2;color:var(--title);text-shadow:1px 1px 2px rgba(0,0,0,.6)}
.notes{position:absolute;left:0;right:0;top:384px;text-align:center;font-family:"Righteous",sans-serif;font-size:9.5px;color:var(--white);line-height:1.35}
.notes .hl{color:var(--title)}
.notes .red{color:var(--red)}
.hours{position:absolute;left:0;right:0;top:468px;text-align:center;font-family:"Black Ops One",sans-serif;color:var(--white)}
.hours .label{display:inline-block;background:var(--green-dark);color:var(--title);font-size:12px;padding:2px 8px;margin-bottom:6px}
.hours .time{font-size:14px}
.band{position:absolute;left:0;right:0;bottom:0;height:36px;background:var(--yellow);display:grid;grid-template-columns:1fr 2fr;align-items:center}
.band-follow{display:flex;align-items:center;justify-content:center;gap:6px;font-family:"Black Ops One",sans-serif;font-size:12px;border-right:1px solid rgba(0,0,0,.3);height:100%}
.band-follow .square{width:16px;height:16px;background:var(--ink);border-radius:3px}
.band-follow .handle{font-family:"Righteous",sans-serif;font-size:10px}
.band-addr{display:grid;grid-template-columns:1fr 1fr;height:100%;align-items:center}
.band-addr p{grid-column:2;text-align:center;font-family:"Righteous",sans-serif;font-size:10px;line-height:1.2}
/* inside */
.inside .box{margin-bottom:10px}
.dish-photos{position:absolute;left:0;right:0;bottom:0;height:70px;background:linear-gradient(90deg,#fff,#e6c79a 30%,#c2562b 55%,#8fbf5c 80%,#fff)}
</style>
</head>
<body>

<section class="sheet sheet--outside" aria-label="Menu outside">
  <div class="panel outside-1">
    <div class="box">
      <h2 class="heading">APPETIZERS</h2>
      <div class="item"><div class="row">Chicharron de Calamares<span class="lead"></span>$12.95</div><p class="desc">(crispy fried calamari served with house tartar sauce and salsa criolla)</p></div>
      <div class="item"><div class="row">Anticucho Carretillero</div><p class="desc">(choice chicken or cow's heart Peruvian style kebabs, served with Cusco corn and grilled potatoes)</p><div class="row sub">Corazon<span class="lead"></span>$15.95</div><div class="row sub">Pollo<span class="lead"></span>$15.95</div></div>
      <div class="item"><div class="row">Palta Rellena</div><p class="desc">(peruvian avocado stuffed with choice of chicken or shrimp, marinated in Peruvian spices)</p><div class="row sub">Camarones<span class="lead"></span>$11.95</div><div class="row sub">Pollo<span class="lead"></span>$8.95</div></div>
      <div class="item"><div class="row">Tamal Criollo<span class="lead"></span>$5.95</div><p class="desc">(peruvian chicken tamale, served with salsa criolla)</p></div>
      <div class="item"><div class="row">Salchipapa<span class="lead"></span>$9.95</div><p class="desc">(french fries mixed with sliced hot dogs)</p></div>
      <div class="item"><div class="row">Papa a la Huancaina<span class="lead"></span>$8.95</div><p class="desc">(boiled potatoes, topped with ají amarillo and queso fresco sauce, egg, olives)</p></div>
      <div class="item"><div class="row">Ocopa Arequipeña<span class="lead"></span>$8.95</div><p class="desc">(boiled potatoes, topped with huacatay sauce and queso fresco, egg, olives)</p></div>
      <div class="item"><div class="row">Empanada Limeña<span class="lead"></span>$3.95</div><p class="desc">(patties stuffed with choice of chicken or beef)</p></div>
      <div class="item"><div class="row">Causa</div><p class="desc">(cold mashed potato infused with key of lime juice, pressed into a cake with choice of chicken or shrimp)</p><div class="row sub">Camarones<span class="lead"></span>$9.95</div><div class="row sub">Pollo<span class="lead"></span>$7.95</div></div>
      <div class="item"><div class="row">Choritos a la Chalaca<span class="lead"></span>$10.95</div><p class="desc">(steamed mussels topped with diced onions, tomatoes, lime juice and Cusco corn)</p></div>
      <div class="item"><div class="row">Piqueo Quenti<span class="lead"></span>$19.95</div><p class="desc">(Dish combined of Chicharron de Calamares, Papa a la Huancaina, Choritos a la Chalaca and Causa)</p></div>
    </div>
  </div>

  <div class="panel outside-2">
    <div class="photo-strip" role="img" aria-label="Photo of dipping sauces in small bowls"></div>
    <div class="photo photo-1" role="img" aria-label="Photo of ceviche with sweet potato"></div>
    <div class="photo photo-2" role="img" aria-label="Photo of empanadas with dipping sauce"></div>
    <div class="box soups">
      <h2 class="heading">SOUPS</h2>
      <div class="item"><div class="row">Aguadito Limeño</div><p class="desc">(chicken and vegetable soup mixed with rice and cilantro)</p><div class="row sub">Large<span class="lead"></span>$9.95</div><div class="row sub">Small<span class="lead"></span>$5.95</div></div>
      <div class="item"><div class="row">Sopa a la Minuta<span class="lead"></span>$12.95</div><p class="desc">(traditional milk and angel's hair pasta soup, served with beef and eggs)</p></div>
      <div class="item"><div class="row">Caldo de Gallina<span class="lead"></span>$12.95</div><p class="desc">(hen broth with noodles, scallion, potatoes and hard-boiled egg)</p></div>
      <div class="item"><div class="row">Chupe de Camarones<span class="lead"></span>$15.95</div><div class="row">Arequipeño</div><p class="desc">(shrimp soup mixed with rice, green peas, Cusco corn, milk, eggs and Peruvian spices)</p></div>
      <div class="item"><div class="row">Parihuela del Puerto<span class="lead"></span>$18.95</div><p class="desc">(classic Peruvian seafood soup)</p></div>
    </div>
  </div>

  <div class="panel outside-3">
    <div class="cover-photo" role="img" aria-label="Photo of fried chicken wings with salad"></div>
    <div class="phone">914-555-0142
      <svg viewBox="0 0 24 24" aria-hidden="true"><circle cx="12" cy="12" r="12" fill="#3f6d10"/><path d="M8 5c1 0 2 3 2 4s-1 1-1 2c1 2 2 3 4 4 1 0 1-1 2-1s4 1 4 2-2 3-3 3C10 19 5 14 5 8c0-1 2-3 3-3z" fill="#f2ee24"/></svg>
    </div>
    <div class="logo">Quenti</div>
    <h1 class="cover-title">Authentic Peruvian<br>Cuisine</h1>
    <div class="notes"><span class="hl">Notes:</span> Deliveries on order of<br><span class="red">$15</span> or more, <span class="red">$5 fee</span><br>for <span class="red">3 miles</span> or more.<br>Chef's specials on weekends.</div>
    <div class="hours"><span class="label">Delivery Hours</span><div class="time">Mon – Sun 11:30 am – 10 pm</div></div>
  </div>

  <div class="band">
    <div class="band-follow">Follow us on <span class="square"></span><span class="handle">@quenti</span></div>
    <div class="band-addr"><p>127 Larkspur St. New Rochelle,<br>NY 10801</p></div>
  </div>
</section>

<section class="sheet sheet--inside inside" aria-label="Menu inside">
  <div class="panel">
    <div class="box">
      <h2 class="heading">SALADS</h2>
      <div class="item"><div class="row">Ensalada de la Casa<span class="lead"></span>$6.95</div><p class="desc">(lettuce, tomatoes, yellow peppers and zucchini)</p></div>
      <div class="item"><div class="row">Ensalada Quenti<span class="lead"></span>$7.95</div><p class="desc">(lettuce, tomatoes, cucumbers, red onions, carrots, radish and avocado)</p></div>
      <div class="item"><div class="row">Ensalada Cesar<span class="lead"></span>$8.95</div><p class="desc">(romaine, lettuce, croutons, parmesan cheese and Quenti's special sauce)</p></div>
    </div>
    <div class="box">
      <h2 class="heading">SIDES</h2>
      <div class="item"><div class="row">Papas Fritas<span class="lead"></span>$3.95</div><p class="desc">(french fries)</p></div>
      <div class="item"><div class="row">Arroz Blanco o Amarillo<span class="lead"></span>$3.95</div><p class="desc">(white/yellow rice)</p></div>
      <div class="item"><div class="row">Frejoles<span class="lead"></span>$3.95</div><p class="desc">(peruvian canario beans)</p></div>
      <div class="item"><div class="row">Maduros<span class="lead"></span>$3.95</div><p class="desc">(sweet plantains)</p></div>
      <div class="item"><div class="row">Tostones<span class="lead"></span>$3.95</div><p class="desc">(fried green plantains)</p></div>
      <div class="item"><div class="row">Yuca Frita<span class="lead"></span>$3.95</div><p class="desc">(fried yuccas)</p></div>
    </div>
    <div class="box" style="height:210px">
      <h2 class="heading">SEAFOOD</h2>
      <div class="item"><div class="row">Pescado a lo Macho<span class="lead"></span>$19.95</div><p class="desc">(fried fish fillet topped with seafood in hot yellow pepper sauce, served with rice and yuccas)</p></div>
      <div class="item"><div class="row">Pescado Sudado<span class="lead"></span>$16.95</div><p class="desc">(corvina fish stew, in hot yellow pepper, tomatoes, onions, served with yuccas and rice)</p></div>
      <div class="item"><div class="row">Arroz con Mariscos<span class="lead"></span>$17.95</div><p class="desc">(peruvian style paella, red rice served with seafood)</p></div>
      <div class="item"><div class="row">Arroz Chaufa</div><p class="desc">(peruvian style fried rice with choice of seafood)</p><div class="row sub">Mariscos<span class="lead"></span>$17.95</div><div class="row sub">Camarones<span class="lead"></span>$18.95</div></div>
    </div>
  </div>

  <div class="panel">
    <div class="box">
      <h2 class="heading">CEVICHES</h2>
      <div class="item"><div class="row">Leche de Tigre<span class="lead"></span>$10.95</div><p class="desc">(ceviche marinade in fresh lime juice)</p></div>
      <div class="item"><div class="row">Tiradito en Salsa de Aji Amarillo<span class="lead"></span>$12.95</div><p class="desc">(sashimi style fish in yellow pepper sauce and fresh lime juice, served with Cusco corn and sweet potatoes)</p></div>
      <div class="item"><div class="row">Piqueo Chalaco<span class="lead"></span>$24.95</div><p class="desc">(dish combined of Ceviche de Pescado and Jalea)</p></div>
      <div class="item"><div class="row">Ceviche</div><p class="desc">(choice of raw fish, mixed seafood, shrimp or octopus, marinated in fresh lime juice)</p><div class="row sub">Pescado<span class="lead"></span>$15.95</div><div class="row sub">Camaron<span class="lead"></span>$17.95</div><div class="row sub">Mixto<span class="lead"></span>$17.95</div><div class="row sub">Camaron con Pulpo<span class="lead"></span>$18.95</div></div>
    </div>
    <div class="box">
      <h2 class="heading">CHICKEN</h2>
      <div class="item"><div class="row">1/4 Pollo<span class="lead"></span>$6.50</div><p class="desc">(quarter chicken, served with two sides)</p></div>
      <div class="item"><div class="row">1/2 Pollo<span class="lead"></span>$8.95</div><p class="desc">(half chicken, served with two sides)</p></div>
      <div class="item"><div class="row">1 Pollo<span class="lead"></span>$16.95</div><p class="desc">(whole chicken, served with two sides)</p></div>
      <div class="item"><div class="row">Pollo Limeño<span class="lead"></span>$20.95</div><p class="desc">(whole chicken, served with fries, avocado salad and yellow rice)</p></div>
      <div class="item"><div class="row">Pollo Quenti<span class="lead"></span>$30.95</div><p class="desc">(whole chicken, served with avocado salad, arroz chaufa and salchipapa)</p></div>
    </div>
    <div class="box">
      <h2 class="heading">DESSERTS</h2>
      <div class="item"><div class="row">Crema Volteada<span class="lead"></span>$5.95</div><p class="desc">(Peruvian caramel custard)</p></div>
      <div class="item"><div class="row">Tres Leches<span class="lead"></span>$5.95</div><p class="desc">(Butter cake soaked in three kinds of milk)</p></div>
      <div class="item"><div class="row">Torta de Chocolate<span class="lead"></span>$5.95</div><p class="desc">(Chocolate cake)</p></div>
      <div class="item"><div class="row">Picarones<span class="lead"></span>$5.95</div><p class="desc">(Peruvian style sweet potato doughnut covered with syrup)</p></div>
    </div>
  </div>

  <div class="panel">
    <div class="box" style="height:486px">
      <h2 class="heading">TRADITIONAL DISHES</h2>
      <div class="item"><div class="row">Parrillada Mixta<span class="lead"></span>$30.95</div><p class="desc">(dish combined of grilled NY Strip steak, anticuchos, pork chops and sausage)</p></div>
      <div class="item"><div class="row">Churrasco en Salsa de Camarones<span class="lead"></span>$20.95</div><p class="desc">(NY strip steak topped with shrimps on hot yellow pepper sauce, served with rice)</p></div>
      <div class="item"><div class="row">Seco Norteño<span class="lead"></span>$20.95</div><p class="desc">(slowly cooked lamb stew in aji panka sauce, served with rice and Peruvian canario beans)</p></div>
      <div class="item"><div class="row">Seco de Pato Piurano<span class="lead"></span>$17.95</div><p class="desc">(slowly cooked duck stew in aji panka sauce, served with rice and yuccas)</p></div>
      <div class="item"><div class="row">Tallarines Verdes con Churrasco<span class="lead"></span>$18.95</div><p class="desc">(linguine pasta in Peruvian style pesto sauce served with grilled NY Strip steak)</p></div>
      <div class="item"><div class="row">Tacu Tacu</div><p class="desc">(peruvian canario beans mixed with rice, served with choice of NY Strip steak or seafood)</p><div class="row sub">Churrasco<span class="lead"></span>$18.95</div><div class="row sub">Lomo<span class="lead"></span>$15.95</div></div>
      <div class="item"><div class="row">Churrasco a lo Pobre<span class="lead"></span>$19.95</div><p class="desc">(NY Strip steak served with fried egg, plantains, fries and rice)</p></div>
      <div class="item"><div class="row">Saltado</div><p class="desc">(choice of beef or chicken mixed with red onions, tomatoes and fries, served with rice)</p><div class="row sub">Lomo<span class="lead"></span>$15.95</div><div class="row sub">Pollo<span class="lead"></span>$13.95</div></div>
      <div class="item"><div class="row">Aeropuerto<span class="lead"></span>$18.95</div><p class="desc">(peruvian style fried rice, mixed with noodles, chicken, beef and shrimp)</p></div>
      <div class="item"><div class="row">Arroz Chaufa</div><p class="desc">(peruvian style fried rice mixed with choice of beef or chicken)</p><div class="row sub">Carne<span class="lead"></span>$14.95</div><div class="row sub">Pollo<span class="lead"></span>$12.95</div></div>
      <div class="item"><div class="row">Seco de Carne<span class="lead"></span>$15.95</div><p class="desc">(beef ribs stew in aji panka sauce, served with rice and Peruvian canario beans)</p></div>
      <div class="item"><div class="row">Aji de Gallina<span class="lead"></span>$11.95</div><p class="desc">(shredded chicken in a spicy aji amarillo creamy sauce, hard-boiled egg, olives, potatoes and rice)</p></div>
    </div>
  </div>
  <div class="dish-photos" role="img" aria-label="Row of photos of plated dishes: salad, fries with sauces, stews and rice"></div>
</section>

</body>
</html>
```